Cool cafe needs help with our corporate identity.

We have a logo! We have a font!

What we need is to tie it together for
1. A menu
2. Labels for jam and other things we sell
3. Business Cards

All should have the same design style.

We have a strong design aesthetic in the cafe. Lots of colour and quirky objects. See this Snapvue profile for photos (you can download high-res from here if you sign into Snapvue): http://www.snapvue-example.com/photos/58216407@K31/

Also our website is www.maudwalrus.example

A main feature is the counter that is made of yardsticks.

There is also a bit of and 80's feel. Especially images of Edmund and Fen (the Royals).

We also like weird taxidermy and anthropology images from the 1920s. Gerald P. Stanwick was an anthropologist who used to own a Walrus called Maud. That is where our name comes from. Google 'Gerald P. Stanwick' for interesting images.

Perhaps design elements could be taken from any of these themes, although we are open to other ideas.

We like being playful and irreverent.

The logo is the words Maud Walrus in Cursive. We want to stick with that. The font we like is Tallow Works Brisk. The logo is currently blue colour - this can change.

1.Menu Specs
We like printing this ourselves. Thick paper A4 with a fold seems to work well. We want some design elements added. Our existing menu is attached.

2. Labels
We have jam jars and labels for biscuits. These are various sizes. It needs to have the name of the jam,e.g. Apricot, The Maud Walrus Logo, Some design elements, A list of ingredients, and the weight. Eg 250g.

3. Business Card
A standard sized business card with The logo, design elements and the following words:
Maud Walrus Cafe
17 Kelvane Street, Ardley North
03 9017 4426
www.maudwalrus.example

Target Market(s)

Adults based in Melbourne, Australia that like design and are kind of hipsterish,

Industry/Entity Type

Printing

Requirements
Must have
• Logo and font as described.
Nice to have
• Maybe a bit quirky.
Should not have
• Slick corporate look.

```html
<!DOCTYPE html>
<html lang="en">
<head>
<meta charset="utf-8">
<title>Maud Walrus Cafe – Menu and Business Cards</title>
<link rel="stylesheet" href="https://fonts.googleapis.com/css2?family=Josefin+Sans:wght@400;600&display=swap">
<style>
  :root {
    --backdrop: #d8d8d8;
    --paper: #ffffff;
    --chevron-blue: #a7c6d6;
    --coral: #ef7e6b;
    --ink: #2b2b2b;
    --ink-soft: #555555;
    --rule: #c9c9c9;
  }
  * { box-sizing: border-box; margin: 0; padding: 0; }
  html, body { width: 1200px; height: 863px; overflow: hidden; }
  body {
    background: var(--backdrop);
    font-family: "Josefin Sans", sans-serif;
    color: var(--ink);
    position: relative;
  }
  .sheet {
    position: absolute;
    background: var(--paper);
    box-shadow: 0 4px 14px rgba(0,0,0,0.18);
    overflow: hidden;
  }
  .chevron-field {
    position: absolute;
    background: var(--chevron-blue);
  }
  .brand-disc {
    position: absolute;
    border-radius: 50%;
    background: var(--coral);
    color: var(--paper);
    display: flex;
    flex-direction: column;
    align-items: center;
    justify-content: center;
    text-align: center;
  }
  .brand-name { font-weight: 400; line-height: 1; }
  .brand-tag { font-weight: 400; letter-spacing: 0.2em; }

  /* Menu cover */
  .menu-cover { left: 40px; top: 40px; width: 340px; height: 481px; }
  .menu-cover .chevron-field { inset: 0; }
  .menu-cover .brand-disc { left: 50px; top: 110px; width: 240px; height: 240px; }
  .menu-cover .brand-name { font-size: 34px; }
  .menu-cover .brand-tag { font-size: 14px; margin-top: 6px; }
  .cover-contact { margin-top: 16px; font-size: 11px; line-height: 1.6; }

  /* Menu inside spread */
  .menu-inside { left: 410px; top: 40px; width: 750px; height: 481px; }
  .menu-inside .chevron-top { left: 0; top: 0; width: 100%; height: 44px; }
  .menu-inside .chevron-edge { right: 0; top: 0; width: 36px; height: 100%; }
  .fold-line { position: absolute; left: 375px; top: 44px; bottom: 0; width: 1px; background: var(--rule); }
  .menu-welcome {
    position: absolute; left: 40px; top: 44px; width: 295px; bottom: 0;
    display: flex; align-items: center; justify-content: center;
    text-align: center; font-size: 14px; line-height: 1.8; color: var(--ink-soft);
  }
  .menu-list {
    position: absolute; left: 410px; top: 70px; width: 280px;
    font-size: 12px;
  }
  .menu-section + .menu-section { margin-top: 16px; }
  .menu-section h2 {
    font-size: 15px; font-weight: 600; color: var(--coral);
    border-bottom: 1px solid var(--rule); padding-bottom: 3px; margin-bottom: 6px;
  }
  .menu-item { display: flex; justify-content: space-between; line-height: 1.75; }
  .menu-item .price { color: var(--ink-soft); }

  /* Business cards */
  .card { top: 600px; width: 330px; height: 213px; }
  .card-front { left: 40px; }
  .card-back { left: 400px; }
  .card-front .brand-disc { left: 30px; top: 46px; width: 70px; height: 70px; }
  .card-front .brand-name { font-size: 12px; }
  .card-front .brand-tag { font-size: 7px; margin-top: 2px; }
  .card-details {
    position: absolute; left: 122px; top: 58px; right: 24px;
    font-size: 11.5px; line-height: 1.75; color: var(--ink-soft);
  }
  .card-details .card-title { font-size: 13px; font-weight: 600; color: var(--ink); border-bottom: 1px solid var(--ink); padding-bottom: 4px; margin-bottom: 6px; }
  .card-back .chevron-field { inset: 0; }
  .card-back .brand-disc { left: 100px; top: 41px; width: 130px; height: 130px; }
  .card-back .brand-name { font-size: 20px; }
  .card-back .brand-tag { font-size: 10px; margin-top: 4px; }
</style>
</head>
<body>

  <section class="sheet menu-cover" aria-label="Menu cover">
    <div class="chevron-field" role="img" aria-label="Light blue and white zigzag chevron pattern"></div>
    <div class="brand-disc">
      <span class="brand-name">Maud Walrus</span>
      <span class="brand-tag">CAFE</span>
      <p class="cover-contact">17 Kelvane Street, Ardley North<br>03 9017 4426<br>www.maudwalrus.example</p>
    </div>
  </section>

  <section class="sheet menu-inside" aria-label="Menu inside">
    <div class="chevron-field chevron-top" role="img" aria-label="Light blue and white zigzag chevron border"></div>
    <div class="chevron-field chevron-edge" role="img" aria-label="Light blue and white zigzag chevron border"></div>
    <div class="fold-line"></div>

    <p class="menu-welcome">Our house is a quirky kind of place,<br>full of odd little treasures.<br>We make it all ourselves with care<br>and serve it with a smile.</p>

    <div class="menu-list">
      <div class="menu-section">
        <h2>Breakfast</h2>
        <p class="menu-item"><span>Jam toast on sourdough</span><span class="price">8</span></p>
        <p class="menu-item"><span>Maud's big breakfast</span><span class="price">19</span></p>
        <p class="menu-item"><span>Bircher muesli with fruit</span><span class="price">12</span></p>
        <p class="menu-item"><span>Eggs your way</span><span class="price">11</span></p>
      </div>
      <div class="menu-section">
        <h2>Lunch</h2>
        <p class="menu-item"><span>Toasted ham sandwich</span><span class="price">13</span></p>
        <p class="menu-item"><span>Soup of the day</span><span class="price">10</span></p>
        <p class="menu-item"><span>Pumpkin and feta salad</span><span class="price">15</span></p>
      </div>
      <div class="menu-section">
        <h2>Sweets</h2>
        <p class="menu-item"><span>Scones with jam</span><span class="price">7</span></p>
        <p class="menu-item"><span>Cake of the day</span><span class="price">6</span></p>
      </div>
      <div class="menu-section">
        <h2>Drinks</h2>
        <p class="menu-item"><span>Coffee</span><span class="price">4</span></p>
        <p class="menu-item"><span>Pot of tea</span><span class="price">5</span></p>
        <p class="menu-item"><span>Fresh juice</span><span class="price">7</span></p>
      </div>
    </div>
  </section>

  <section class="sheet card card-front" aria-label="Business card front">
    <div class="brand-disc">
      <span class="brand-name">Maud Walrus</span>
      <span class="brand-tag">CAFE</span>
    </div>
    <div class="card-details">
      <p class="card-title">Maud Walrus Cafe</p>
      <p>17 Kelvane Street, Ardley North</p>
      <p>03 9017 4426</p>
      <p>www.maudwalrus.example</p>
    </div>
  </section>

  <section class="sheet card card-back" aria-label="Business card back">
    <div class="chevron-field" role="img" aria-label="Light blue and white zigzag chevron pattern"></div>
    <div class="brand-disc">
      <span class="brand-name">Maud Walrus</span>
      <span class="brand-tag">CAFE</span>
    </div>
  </section>

</body>
</html>
```